Property Management Company Business Cards

Need business cards for a property management company located in Michigan. We manage houses for clients all over the world. Young and modern company, looking for eye catching design. Please work with the attached logo.

Industry/Entity Type

Property Management

Requirements
Must have
• Need lines for address, telephone number, fax number, web site.

Also lines for name, and job title

```html
<!DOCTYPE html>
<html lang="en">
<head>
<meta charset="utf-8">
<title>Harborline Global Management – Business Cards</title>
<link rel="stylesheet" href="https://fonts.googleapis.com/css2?family=Open+Sans:wght@300;400;600;700&display=swap">
<style>
  :root {
    --page: #e9e6e1;
    --card-white: #ffffff;
    --card-black: #050505;
    --ink: #3a3a3c;
    --ink-soft: #5c5c60;
    --accent: #58a6e6;
    --rule: #9a9a9e;
    --on-dark: #f2f2f2;
  }
  * { margin: 0; padding: 0; box-sizing: border-box; }
  html, body {
    width: 1200px; height: 900px; overflow: hidden;
    background: var(--page);
    font-family: "Open Sans", Arial, sans-serif;
  }
  .canvas {
    width: 1200px; height: 900px;
    display: flex; flex-direction: column; align-items: center; justify-content: center;
    gap: 56px;
  }
  .card {
    position: relative;
    width: 640px; height: 366px;
    box-shadow: 0 10px 28px rgba(0,0,0,.22);
    overflow: hidden;
  }
  .card--front { background: var(--card-white); }
  .card--back { background: var(--card-black); }

  .brand { position: absolute; display: flex; align-items: center; gap: 14px; }
  .brand__dot { width: 46px; height: 46px; border-radius: 50%; background: var(--accent); flex: none; }
  .brand__name {
    font-weight: 700; font-size: 30px; line-height: 1.05;
    text-transform: uppercase; letter-spacing: .5px;
    border-left: 2px solid currentColor; padding-left: 12px;
  }
  .card--front .brand { left: 40px; top: 40px; }
  .card--front .brand__name { color: var(--ink); }
  .card--back .brand { left: 48px; top: 140px; }
  .card--back .brand__name { color: var(--on-dark); }

  .person__name {
    position: absolute; right: 40px; top: 132px;
    font-weight: 600; font-size: 30px; color: var(--accent);
  }
  .divider {
    position: absolute; left: 40px; right: 40px; top: 178px;
    border-top: 1px solid var(--rule);
  }
  .person__title {
    position: absolute; right: 40px; top: 186px;
    font-weight: 300; font-size: 18px; color: var(--ink-soft);
  }
  .contact {
    position: absolute; left: 40px; top: 208px;
    list-style: none; font-size: 15px; font-weight: 400; color: var(--ink);
  }
  .contact li { display: flex; align-items: center; gap: 10px; height: 23px; }
  .contact svg { width: 13px; height: 13px; fill: var(--ink); flex: none; }
  .contact .no-icon { padding-left: 23px; }
  .band {
    position: absolute; left: 0; right: 0; bottom: 0; height: 30px;
    background: var(--accent);
  }
  .back__web {
    position: absolute; right: 48px; bottom: 40px;
    font-size: 16px; font-weight: 400; color: var(--on-dark);
  }
</style>
</head>
<body>
<main class="canvas">
  <section class="card card--front">
    <div class="brand">
      <span class="brand__dot"></span>
      <span class="brand__name">Harborline Global<br>Management</span>
    </div>
    <p class="person__name">Tesfaye Alemu</p>
    <hr class="divider">
    <p class="person__title">Managing Director</p>
    <ul class="contact">
      <li class="no-icon">xxxx Elmcrest Dr. Suite 102</li>
      <li><svg viewBox="0 0 16 16"><path d="M3 1h3l1.5 4-2 1.3a9 9 0 0 0 4.2 4.2l1.3-2 4 1.5v3c0 1-1 2-2 2C6.5 15 1 9.5 1 3c0-1 1-2 2-2z"/></svg>xxx-xxx-xxxx</li>
      <li><svg viewBox="0 0 16 16"><path d="M4 1h7v4H4zM1 6h14v7h-3v2H4v-2H1zm4 5v3h6v-3z"/></svg>xxx-xxx-xxxx</li>
      <li><svg viewBox="0 0 16 16"><path d="M1 3h14v10H1zm1.5 1.2V5l5.5 4 5.5-4v-.8z"/></svg>info@harborlineglobal.com</li>
      <li><svg viewBox="0 0 16 16"><path d="M8 1a7 7 0 1 0 0 14A7 7 0 0 0 8 1zm0 1.5c.8 0 1.8 1.7 2 4.5H6c.2-2.8 1.2-4.5 2-4.5zM2.6 7a5.5 5.5 0 0 1 2.6-4A10 10 0 0 0 4.5 7zm0 2h1.9c.1 1.6.4 3 .7 4A5.5 5.5 0 0 1 2.6 9zM6 9h4c-.2 2.8-1.2 4.5-2 4.5S6.2 11.8 6 9zm5.5 0h1.9a5.5 5.5 0 0 1-2.6 4c.3-1 .6-2.4.7-4zm0-2c-.1-1.6-.4-3-.7-4a5.5 5.5 0 0 1 2.6 4z"/></svg>www.harborlineglobal.com</li>
    </ul>
    <div class="band"></div>
  </section>

  <section class="card card--back">
    <div class="brand">
      <span class="brand__dot"></span>
      <span class="brand__name">Harborline Global<br>Management</span>
    </div>
    <p class="back__web">www.harborlineglobal.com</p>
  </section>
</main>
</body>
</html>
```